Stationery Design Project - Professional Training Company

Full set of statinery in PDF and format that can be given to the printers

Letterhead
Business cards x 3
Compliments slip
Envelope
Updates

Many thanks for all your contributions, the quality of the designs is amazing.

Thank you all so much for your contribution to this project, I am very impressed with the designs and choice of designs, you are all clearly very talented individuals.

I hope to be making a decision on the final choice this evening UAE time.

Best regards and again thank you so much

Gordon

I would like to take this opportunity to thank you all for your contributions, I have been very impressed with each of the designs submitted.

I will shortly go back and give each of you a personal rating on each of your designs.

Again thank you all so much for your efforts

Best Regards

Gordon

Target Market(s)

We are a training company that provides IT training for Medical and Professional Staff, we train professional adults

Industry/Entity Type

Business

Requirements
Must have
• The letterhead and compliments slip must have at the bottom of the page:-

Bright Ledger Pathways LLP operates as a limited liability partnership registered in England and Wales (with registered number OC702614)

Business Cards are to be made up for three people (details of those to be provided after appoval of design but are included in this project) and should contain:

Name
Title
Telephone
email
Address: P.O. Box 418263 Dubai UAE
web address: www.brightledgerpathways.example
Nice to have
• Very clean and professional looking
Should not have
• No look to busy or ovr crowded

```html
<!DOCTYPE html>
<html lang="en">
<head>
<meta charset="utf-8">
<title>Bright Ledger Pathways LLP – Business Card</title>
<link href="https://fonts.googleapis.com/css2?family=Source+Sans+3:wght@400;600;700&display=swap" rel="stylesheet">
<style>
  :root {
    --page-bg: #e6e6e6;
    --plum: #7a1470;
    --plum-deep: #4a0b45;
    --plum-light: #9a2290;
    --leaf: #4e9a1e;
    --ink: #2f2f33;
    --ink-soft: #4a4a50;
    --rule: #b9b9bd;
    --paper: #f7f7f5;
    --white: #ffffff;
  }
  * { box-sizing: border-box; margin: 0; padding: 0; }
  html, body {
    width: 1200px; height: 900px; overflow: hidden;
    background: var(--page-bg);
    font-family: "Source Sans 3", "Myriad Pro", Arial, sans-serif;
  }
  .canvas { position: relative; width: 1200px; height: 900px; }

  .card {
    position: absolute; left: 300px; width: 600px; height: 343px;
    box-shadow: 0 6px 18px rgba(0,0,0,0.18);
    overflow: hidden;
  }

  .brand {
    display: flex; align-items: center; gap: 14px;
    font-weight: 600; letter-spacing: -0.3px; line-height: 0.95;
  }
  .brand-dot { flex: none; border-radius: 50%; }

  /* Front */
  .card-front {
    top: 70px;
    background: radial-gradient(ellipse at 55% 45%, var(--plum-light) 0%, var(--plum) 45%, var(--plum-deep) 100%);
    display: flex; align-items: center; justify-content: center;
  }
  .card-front .brand { color: var(--white); font-size: 26px; }
  .card-front .brand-dot { width: 34px; height: 34px; background: var(--white); }

  /* Back */
  .card-back { top: 487px; background: var(--paper); }
  .card-back .brand {
    position: absolute; left: 38px; top: 58px;
    color: var(--ink); font-size: 30px;
  }
  .card-back .brand-dot { width: 40px; height: 40px; background: var(--plum); }

  .holder { position: absolute; right: 38px; top: 56px; text-align: right; }
  .holder-name { color: var(--plum); font-size: 20px; font-weight: 700; line-height: 1; }
  .holder-title { color: var(--ink); font-size: 13px; margin-top: 3px; }

  .divider {
    position: absolute; left: 38px; right: 38px; top: 158px;
    height: 1px; background: var(--rule);
  }

  .contacts { position: absolute; left: 38px; top: 180px; list-style: none; }
  .contacts li {
    display: flex; align-items: center; gap: 10px;
    color: var(--ink); font-size: 15px; line-height: 23px;
  }
  .contacts svg { width: 14px; height: 14px; fill: var(--ink-soft); flex: none; }

  .address {
    position: absolute; right: 38px; top: 180px; text-align: right;
    color: var(--ink-soft); font-size: 14px; line-height: 19px; font-style: normal;
  }

  .accent-line { position: absolute; left: 0; right: 0; top: 296px; height: 3px; background: var(--leaf); }
  .accent-band {
    position: absolute; left: 0; right: 0; top: 299px; bottom: 0;
    background: linear-gradient(90deg, var(--plum-deep), var(--plum) 60%, var(--plum-light));
  }
</style>
</head>
<body>
<main class="canvas">

  <section class="card card-front" aria-label="Business card front">
    <div class="brand">
      <span class="brand-dot"></span>
      <span class="brand-name">Bright Ledger<br>Pathways LLP</span>
    </div>
  </section>

  <section class="card card-back" aria-label="Business card back">
    <div class="brand">
      <span class="brand-dot"></span>
      <span class="brand-name">Bright Ledger<br>Pathways LLP</span>
    </div>

    <div class="holder">
      <p class="holder-name">Rashid Harlan</p>
      <p class="holder-title">President</p>
    </div>

    <div class="divider"></div>

    <ul class="contacts">
      <li>
        <svg viewBox="0 0 16 16" aria-hidden="true"><path d="M3.5 1.5l2.5 0 1 3.5-1.8 1.2a8 8 0 0 0 4.6 4.6L11 9l3.5 1v2.5c0 1-1 2-2 2A11 11 0 0 1 1.5 3.5c0-1 1-2 2-2z"/></svg>
        +971 (2) 5504127
      </li>
      <li>
        <svg viewBox="0 0 16 16" aria-hidden="true"><path d="M4 1h8v4H4zM2 6h12a1 1 0 0 1 1 1v5h-3v3H4v-3H1V7a1 1 0 0 1 1-1zm3 5v3h6v-3z"/></svg>
        +971 (2) 5504127
      </li>
      <li>
        <svg viewBox="0 0 16 16" aria-hidden="true"><path d="M8 1a7 7 0 1 0 3.5 13.1l-.6-1.2A5.7 5.7 0 1 1 13.7 8c0 1.3-.6 2-1.3 2s-1-.5-1-1.2V4.5h-1.3v.7A3.2 3.2 0 1 0 10.4 10c.4.8 1.1 1.3 2 1.3 1.6 0 2.6-1.4 2.6-3.3A7 7 0 0 0 8 1zm0 9a2 2 0 1 1 0-4 2 2 0 0 1 0 4z"/></svg>
        harlan@brightledgerpathways.example
      </li>
      <li>
        <svg viewBox="0 0 16 16" aria-hidden="true"><path d="M8 1a7 7 0 1 0 0 14A7 7 0 0 0 8 1zm4.9 6.3h-2.3a11 11 0 0 0-.9-4.3 5.6 5.6 0 0 1 3.2 4.3zM8 2.6c.7.9 1.2 2.6 1.3 4.7H6.7c.1-2.1.6-3.8 1.3-4.7zM6.3 3a11 11 0 0 0-.9 4.3H3.1A5.6 5.6 0 0 1 6.3 3zM3.1 8.7h2.3c.1 1.6.4 3.1.9 4.3a5.6 5.6 0 0 1-3.2-4.3zM8 13.4c-.7-.9-1.2-2.6-1.3-4.7h2.6c-.1 2.1-.6 3.8-1.3 4.7zm1.7-.4c.5-1.2.8-2.7.9-4.3h2.3A5.6 5.6 0 0 1 9.7 13z"/></svg>
        www.brightledgerpathways.example
      </li>
    </ul>

    <address class="address">
      P.O. Box 418263 Dubai<br>
      United Arab Emirates
    </address>

    <div class="accent-line"></div>
    <div class="accent-band"></div>
  </section>

</main>
</body>
</html>
```